Psychologist in Private Practice Needs a Website Update

Project Description:
Hello talented designers! My current website, www.jodelbrisk.com, needs a fresh, boho-modern makeover that highlights the warm, welcoming nature of my holistic therapy practice. I want a website that has a serene, boho- modern design, appealing to clients seeking individual therapy, couples therapy, and family counseling.

I’d also like to prepare for a future second site focused exclusively on couples and family therapy. Both sites should be interconnected, so I’m looking for design suggestions that seamlessly link them together while maintaining a cohesive brand look and feel.

Key Objectives:

Boho-Modern Aesthetic: Incorporate natural textures, neutral or earthy tones, and clean lines that capture a modern, inviting vibe.

Responsive Design: Ensure the website is user-friendly on desktop, tablet, and mobile devices.

Clear Service Offerings: Prominently feature my three distinct services: individual therapy, couples therapy, and family counseling.

Interlinked Future Site: Provide ideas on how to cross-link this site with a second site focused on couples and family therapy.

User Experience (UX): Make the site simple to navigate, with intuitive placement of content that speaks to potential clients’ needs.

SEO-Friendly: Implement best practices for structure, site speed, and keyword usage to boost online visibility.

What I Have Now:
Existing website: www.jodelbrisk.com
Basic content and a logo that can be refined or updated to match the boho-modern feel
Rough style guide with brand elements open to a fresh interpretation

Preferred Style/Tone:
Boho-modern with earthy tones, subtle textures, and clean typography
Warm, empathetic, and approachable to align with the nature of therapy services
Slightly artistic or organic elements that evoke calm and connection

Potential for an ongoing design relationship!
Updates

Need extra days to review

Target Market(s)

I have a high functioning, professional clientele who doctors, lawyers, and leaders in their field.

Industry/Entity Type

healthcare/mental health

Coding

Coded - Design and coding required

Font styles to use
Other font styles liked:
• cormorant garamond for headers and Source Sans Pro for supporting text

Colors

Designer to choose colors to be used in the design.

Requirements
Must have
• Open, Harmonious Layout I’d like the overall design to feel upscale, humanistic, open and harmonious, with minimal divisions of space. Rather than traditional section dividers, please consider using images, subtle shifts in color, typography, or spacing to define sections. Hero Image & Inspiration Ideally, the first (hero) image should evoke a sense of awe or inspiration. Focus on simplicity and elegance so the design feels spacious and inviting, allowing the content and imagery to really stand out. Natural Flow Wherever possible, let the design elements flow naturally into each other, creating a sense of unity and cohesion throughout the site.
Nice to have
• 1. Full-Width Hero Image: • The homepage should feature a full-width hero image that extends edge-to-edge across the screen for a modern and visually immersive effect. • This image should set the tone for the website, reflecting a calming, humanistic/natural, and upscale feel. It could include subtle overlays or gradients to enhance readability of text and navigation elements. Ideally, this image should have one or two people in nature. The image could be slightly transparent to allow the text "holistic therapy" and the tagline "an integrative approach to transformation" to be easily visible. Please help me find a breath-taking image that evokes a sense of beauty, inspiration, awe or hope. 2. Menu Tabs Positioned Over the Image: • The menu tabs (navigation bar) should be positioned directly on top of the hero image, either centered or aligned to the top right/left, depending on the design. • The navigation bar should have a slightly transparent or solid background (depending on the image and visibility needs) to ensure the text is easily readable without detracting from the image. 3. Typography and Text Placement: • The text overlay on the hero image should use the selected fonts: • Cormorant Garamond for headers (e.g., the tagline or welcome message). • Source Sans Pro for any supporting text. 5. Seamless Transitions: • Below the full-width image, transitions into the next sections (like “About,” “Services,” or client-focused content) should be smooth, using full-width separators that maintain the cohesive, open layout style. 6. Color Palette: • A neutral and calming color palette should be used (e.g., soft blues, grays, whites, or very muted earth tones) to create a soothing atmosphere for visitors. This design approach ensures the homepage looks clean, modern, and professional while maintaining the calming and upscale aesthetic that reflects the values of my psychology practice

```html
<!DOCTYPE html>
<html lang="en">
<head>
<meta charset="utf-8">
<title>Dr. Jodel Brisk – Licensed Psychologist</title>
<link href="https://fonts.googleapis.com/css2?family=Lato:wght@400;700;900&family=Source+Sans+3:wght@400;600;700&display=swap" rel="stylesheet">
<style>
:root{
  --green:#8ba65b;
  --green-dark:#6f8b45;
  --teal:#3d8a88;
  --ink:#2a2a2a;
  --text:#5d5d5d;
  --muted:#8a8a8a;
  --soft:#f3f3ef;
  --white:#ffffff;
  --footer:#2d2d2d;
  --footer-deep:#222222;
}
*{box-sizing:border-box;margin:0;padding:0}
html,body{width:1200px;height:4116px;overflow:hidden;background:var(--white)}
body{font-family:"Source Sans 3",Arial,sans-serif;color:var(--text)}
.page{position:relative;width:1200px;height:4116px;overflow:hidden}
.abs{position:absolute}
h1,h2,h3,.brand,.nav,.btn{font-family:"Lato",Arial,sans-serif}

/* header */
.site-header{position:absolute;left:0;top:0;width:1200px;height:80px;background:var(--white);z-index:5}
.brand{position:absolute;left:100px;top:12px;color:var(--ink);line-height:1.05}
.brand-name{font-size:27px;font-weight:400}
.brand-sub{font-size:19px;font-weight:400}
.nav{position:absolute;left:440px;top:30px;display:flex;gap:26px;font-size:15px;font-weight:700;color:var(--ink);letter-spacing:.5px}
.nav .active{color:var(--green);position:relative}
.nav .active::after{content:"";position:absolute;left:6px;right:6px;bottom:-8px;height:2px;background:var(--green)}
.login{position:absolute;left:930px;top:14px;width:160px;height:48px;border-radius:8px;background:var(--green);color:var(--white);font-size:16px;font-weight:700;display:flex;align-items:center;justify-content:center;gap:10px}

/* hero */
.hero{position:absolute;left:0;top:80px;width:1200px;height:660px;background:linear-gradient(180deg,#f2c98a 0%,#e8b774 22%,#b9a16a 40%,#7e8f4a 58%,#5f7a34 75%,#4c6a2a 100%)}
.hero-copy{position:absolute;left:0;top:80px;width:1200px;text-align:center;color:var(--white)}
.hero-copy .eyebrow{font-family:"Lato",sans-serif;font-size:46px;font-weight:400;letter-spacing:2px}
.hero-copy h1{font-size:66px;font-weight:900;letter-spacing:1px;line-height:1.05}
.hero-copy .role{font-family:"Lato",sans-serif;font-size:32px;letter-spacing:2px;margin-top:4px}
.btn{display:inline-flex;align-items:center;justify-content:center;background:var(--green);color:var(--white);font-size:15px;font-weight:700;border-radius:8px;letter-spacing:.5px}
.hero-copy .btn{margin-top:32px;width:238px;height:54px}
.hero-wave{position:absolute;left:0;top:600px;width:1200px;height:150px}

/* section headings */
.section-title{position:absolute;left:0;width:1200px;text-align:center;font-size:42px;font-weight:900;color:var(--ink);letter-spacing:1px;line-height:1.2}
.section-title span,.title-left span{color:var(--green)}

/* cards */
.card{position:absolute;width:300px;background:var(--white);box-shadow:0 4px 18px rgba(0,0,0,.12);text-align:center}
.card-photo{height:176px}
.card h3{font-size:16px;font-weight:900;color:var(--ink);margin:18px 0 10px;text-transform:uppercase}
.card p{font-size:14px;line-height:1.45;padding:0 22px;color:var(--text)}
.card .arrow{margin:14px auto 18px;display:block}
.slider-arrow{position:absolute;width:40px;height:40px;border-radius:50%;background:var(--teal);display:flex;align-items:center;justify-content:center}
.slider-arrow.outline{background:var(--white);border:2px solid var(--teal)}

/* about */
.about{position:absolute;left:0;top:1340px;width:1200px;height:520px;background:var(--soft)}
.about-photo{position:absolute;left:0;top:0;width:500px;height:520px;background:linear-gradient(160deg,#e9e5dc 0%,#d9b79a 45%,#b57a52 70%,#8c5a3c 100%)}
.title-left{font-size:40px;font-weight:900;color:var(--ink);letter-spacing:1px;white-space:nowrap}
.about-body{position:absolute;left:600px;top:60px;width:520px}
.about-body .sub{font-family:"Lato",sans-serif;font-size:15px;font-weight:700;color:var(--ink);margin:14px 0 14px;letter-spacing:.5px}
.about-body p{font-size:15px;line-height:1.6}
.about-body .btn{margin-top:28px;width:130px;height:46px;font-size:14px}

/* issues band */
.issues{position:absolute;left:0;top:1860px;width:1200px;height:560px;background:var(--green);overflow:hidden}
.issues h2{position:absolute;left:0;top:70px;width:1200px;text-align:center;color:var(--white);font-size:40px;font-weight:900;line-height:1.2;letter-spacing:1px}
.issue-label{position:absolute;color:var(--white);font-family:"Lato",sans-serif;font-size:13px;font-weight:900;line-height:1.35;letter-spacing:.3px}
.center-badge{position:absolute;left:410px;top:430px;width:380px;text-align:center;color:var(--ink)}
.center-badge .name{font-family:"Lato",sans-serif;font-size:29px}
.center-badge .sub{font-family:"Lato",sans-serif;font-size:21px}
.center-badge .btn{margin-top:14px;width:128px;height:42px;font-size:13px}

/* partnership */
.partner-copy{position:absolute;left:100px;top:2560px;width:470px}
.partner-copy .title-left{font-size:34px}
.partner-copy p{font-size:15px;line-height:1.65;margin-top:30px}
.partner-copy .btn{margin-top:50px;width:136px;height:48px;font-size:14px}
.partner-photo{position:absolute;left:600px;top:2560px;width:490px;height:410px;border-radius:0 0 0 90px;background:linear-gradient(150deg,#efe6dc 0%,#d8c3b0 40%,#b08b74 75%,#7d6a5f 100%)}
.partner-accent{position:absolute;left:560px;top:2820px;width:110px;height:190px;background:var(--green);border-radius:0 0 0 60px}

/* blog */
.blog-card{position:absolute;width:300px;text-align:left}
.blog-card .card-photo{height:186px}
.blog-card h3{font-size:14px;font-weight:900;color:var(--ink);margin:18px 0 8px;line-height:1.3;text-transform:uppercase}
.blog-card p{font-size:14px;line-height:1.5}
.blog-card .more{display:inline-block;margin-top:12px;font-family:"Lato",sans-serif;font-size:14px;font-weight:700;color:var(--green);text-decoration:underline}

/* footer */
.site-footer{position:absolute;left:0;top:3780px;width:1200px;height:292px;background:var(--footer);color:#d8d8d8}
.footer-brand{position:absolute;left:100px;top:34px;color:var(--white);font-family:"Lato",sans-serif;line-height:1.05}
.footer-brand .brand-name{font-size:27px}
.footer-brand .brand-sub{font-size:19px}
.footer-brand p{font-family:"Source Sans 3",sans-serif;font-size:13px;color:#cfcfcf;line-height:1.5;margin-top:14px;width:250px}
.footer-col{position:absolute;top:36px}
.footer-col h4{font-family:"Lato",sans-serif;font-size:18px;font-weight:900;color:var(--white);letter-spacing:.5px;margin-bottom:20px}
.footer-col li{list-style:none;font-size:15px;margin-bottom:16px;text-transform:uppercase}
.contact-item{display:flex;gap:14px;align-items:flex-start;margin-bottom:18px}
.contact-icon{flex:0 0 34px;height:34px;border-radius:50%;background:var(--teal);display:flex;align-items:center;justify-content:center}
.contact-item b{display:block;font-family:"Lato",sans-serif;font-size:13px;color:var(--white)}
.contact-item span{font-size:13px;text-transform:uppercase;line-height:1.35}
.social{display:flex;gap:12px}
.social i{width:30px;height:30px;border-radius:50%;border:2px solid #bdbdbd}
.social i.on{background:var(--teal);border-color:var(--teal)}
.copyright{position:absolute;left:0;top:4072px;width:1200px;height:44px;background:var(--footer-deep);color:#cfcfcf;font-size:14px;display:flex;align-items:center;justify-content:center}
</style>
</head>
<body>
<div class="page">

<header class="site-header">
  <div class="brand"><div class="brand-name">Dr. Jodel Brisk</div><div class="brand-sub">Licensed Psychologist</div></div>
  <nav class="nav"><span class="active">HOME</span><span>ABOUT US</span><span>SERVICE</span><span>FAQS</span><span>BLOG</span></nav>
  <div class="login">
    <svg width="18" height="18" viewBox="0 0 18 18"><circle cx="9" cy="6" r="4" fill="none" stroke="#fff" stroke-width="2"/><path d="M2 17c1-4 4-6 7-6s6 2 7 6" fill="none" stroke="#fff" stroke-width="2"/></svg>
    LOGIN
  </div>
</header>

<section class="hero">
  <div class="abs" role="img" aria-label="Sunlit green hills and mountain valley at golden hour" style="inset:0"></div>
  <div class="hero-copy">
    <div class="eyebrow">WELCOME TO</div>
    <h1>DR. JODEL BRISK</h1>
    <div class="role">LICENSED PSYCHOLOGIST</div>
    <span class="btn">GET AN APPOINTMENT</span>
  </div>
</section>
<svg class="hero-wave" viewBox="0 0 1200 150" preserveAspectRatio="none">
  <path d="M0 70 C260 10 520 120 760 70 C960 30 1100 40 1200 60 L1200 150 L0 150Z" fill="#3d8a88" opacity=".85"/>
  <path d="M0 90 C280 40 520 140 780 92 C980 56 1110 70 1200 86 L1200 150 L0 150Z" fill="#8ba65b"/>
  <path d="M0 104 C300 62 540 150 800 108 C990 78 1110 92 1200 104 L1200 150 L0 150Z" fill="#ffffff"/>
</svg>

<h2 class="section-title" style="top:770px">OUR <span>SERVICES</span></h2>

<article class="card" style="left:110px;top:862px">
  <div class="card-photo" role="img" aria-label="Therapist listening to a client in a bright office" style="background:linear-gradient(135deg,#e8ddd2,#b99a83)"></div>
  <h3>Individual Therapy</h3>
  <p>We work with adults age 18+ using a highly personalized and flexible approach tailored to each client's individual needs. Dr. Jodel Brisk and her associates.</p>
  <svg class="arrow" width="22" height="14" viewBox="0 0 22 14"><path d="M1 7h18M13 1l6 6-6 6" fill="none" stroke="#8ba65b" stroke-width="2.2"/></svg>
</article>
<article class="card" style="left:450px;top:862px">
  <div class="card-photo" role="img" aria-label="Couple in a counseling session" style="background:linear-gradient(135deg,#dfe3e6,#9ea9ad)"></div>
  <h3>Couples Therapy</h3>
  <p>Relationships are the heart of the human experience. Instead of giving couples and families advice, we help them to look underneath anger, frustration.</p>
  <svg class="arrow" width="22" height="14" viewBox="0 0 22 14"><path d="M1 7h18M13 1l6 6-6 6" fill="none" stroke="#8ba65b" stroke-width="2.2"/></svg>
</article>
<article class="card" style="left:790px;top:862px">
  <div class="card-photo" role="img" aria-label="Family sitting together on a sofa" style="background:linear-gradient(135deg,#eadfd3,#c2a48a)"></div>
  <h3>Family Counseling</h3>
  <p>Relationships are the heart of the human experience. Instead of giving couples and families advice, we help them to look underneath anger, frustration.</p>
  <svg class="arrow" width="22" height="14" viewBox="0 0 22 14"><path d="M1 7h18M13 1l6 6-6 6" fill="none" stroke="#8ba65b" stroke-width="2.2"/></svg>
</article>
<div class="slider-arrow" style="left:40px;top:1044px"><svg width="14" height="14" viewBox="0 0 14 14"><path d="M9 2 4 7l5 5" fill="none" stroke="#fff" stroke-width="2.4"/></svg></div>
<div class="slider-arrow outline" style="left:1116px;top:1044px"><svg width="14" height="14" viewBox="0 0 14 14"><path d="M5 2l5 5-5 5" fill="none" stroke="#3d8a88" stroke-width="2.4"/></svg></div>

<section class="about">
  <div class="about-photo" role="img" aria-label="Portrait of Dr. Jodel Brisk"></div>
  <div class="about-body">
    <h2 class="title-left">ABOUT <span>DR. JODEL BRISK</span></h2>
    <div class="sub">OWNER, LICENSED CLINICAL PSYCHOLOGIST</div>
    <p>I earned my Doctor of Psychology (Psy.D.) in Clinical Psychology from Halvern University. In addition to my private practice in Cedar Hollow, where I served as the Director of Counseling at Westbrook College, I oversee all aspects of counseling services, including outreach programming, crisis intervention, individual and group psychotherapy, as well as consultation with parents, faculty, and staff. Furthermore, I provide clinical supervision.</p>
    <span class="btn">READ MORE</span>
  </div>
</section>

<section class="issues">
  <h2>ARE YOU STRUGGLING WITH ISSUES THAT<br>AFFECT THE WAY YOU LIVE, LOVE OR WORK?</h2>
  <svg class="abs" style="left:0;top:0" width="1200" height="560" viewBox="0 0 1200 560">
    <path d="M330 560 A270 270 0 0 1 870 560" fill="none" stroke="#fff" stroke-width="3"/>
    <path d="M400 560 A200 200 0 0 1 800 560Z" fill="#fff"/>
    <g fill="#fff">
      <circle cx="600" cy="290" r="26"/><circle cx="402" cy="372" r="26"/><circle cx="798" cy="372" r="26"/>
      <circle cx="350" cy="488" r="26"/><circle cx="850" cy="488" r="26"/>
    </g>
    <g fill="none" stroke="#8ba65b" stroke-width="2.4">
      <path d="M600 300c-8-6-12-10-12-15a6 6 0 0 1 12-2 6 6 0 0 1 12 2c0 5-4 9-12 15z"/>
      <circle cx="396" cy="372" r="6"/><circle cx="408" cy="372" r="6"/>
      <circle cx="798" cy="368" r="7"/><path d="M788 384c2-6 18-6 20 0"/>
      <path d="M340 488h20M350 478v20"/>
      <path d="M843 482l7-6 7 6v10h-14z"/>
    </g>
  </svg>
  <div class="issue-label" style="left:520px;top:212px;width:160px;text-align:center">PARENT A CHILD WITH COMPLEX NEEDS.</div>
  <div class="issue-label" style="left:110px;top:352px;width:260px;text-align:right">EXPERIENCE A LACK OF CONNECTION IN YOUR MARRIAGE.</div>
  <div class="issue-label" style="left:836px;top:352px;width:240px">WORRY EXCESSIVELY ABOUT WHAT OTHERS THINK.</div>
  <div class="issue-label" style="left:70px;top:470px;width:250px;text-align:right">FEEL OVERWHELMED WITH DEPRESSION OR ANXIETY.</div>
  <div class="issue-label" style="left:890px;top:470px;width:200px">HAVE A HISTORY OF TRAUMA OR ABUSE.</div>
  <div class="center-badge">
    <div class="name">Dr. Jodel Brisk</div>
    <div class="sub">Licensed Psychologist</div>
    <span class="btn">LEARN MORE</span>
  </div>
</section>

<div class="partner-copy">
  <h2 class="title-left">THERAPY IS A <span>PARTNERSHIP</span></h2>
  <p>Our clinicians utilize contemporary neuroscience-informed therapies along with the wisdom of traditional psychotherapy to foster insight, mindfulness, self-compassion, and deeper connections to oneself and others. Together, in a safe and non-judgmental environment, we will work to understand what holds you back from living the life you really want. All are welcome and celebrated.</p>
  <span class="btn">READ MORE</span>
</div>
<div class="partner-accent"></div>
<div class="partner-photo" role="img" aria-label="Therapist and child holding mood cards during a session"></div>

<h2 class="section-title" style="top:3118px">OUR <span>LATEST BLOGS</span></h2>

<article class="blog-card" style="left:110px;top:3210px">
  <div class="card-photo" role="img" aria-label="Couple talking at a kitchen table" style="background:linear-gradient(135deg,#d9e2e4,#8fa2a6)"></div>
  <h3>Communication in Relationships: Getting to the Heart of the Issue</h3>
  <p>When couples say communication in relationships is their primary problem, they are missing opportunities to truly learn to understand each other.</p>
  <span class="more">READ MORE</span>
</article>
<article class="blog-card" style="left:450px;top:3210px">
  <div class="card-photo" role="img" aria-label="Counselor speaking with a young client" style="background:linear-gradient(135deg,#e6ded4,#b2a08e)"></div>
  <h3>Lorem ipsum dolor sit amet, consectetur adipiscing</h3>
  <p>Lorem ipsum dolor sit amet, sed diam nonumy eirmod tempor ut labore et dolore magna aliqua. Ut enim ad minim veniam, quis nostrud amet.</p>
  <span class="more">READ MORE</span>
</article>
<article class="blog-card" style="left:790px;top:3210px">
  <div class="card-photo" role="img" aria-label="Family gathered in a living room" style="background:linear-gradient(135deg,#ece2d6,#bf9f84)"></div>
  <h3>Lorem ipsum dolor sit amet, consectetur adipiscing</h3>
  <p>Lorem ipsum dolor sit amet, sed diam nonumy eirmod tempor ut labore et dolore magna aliqua. Ut enim ad minim veniam, quis nostrud amet.</p>
  <span class="more">READ MORE</span>
</article>
<div class="slider-arrow" style="left:40px;top:3410px"><svg width="14" height="14" viewBox="0 0 14 14"><path d="M9 2 4 7l5 5" fill="none" stroke="#fff" stroke-width="2.4"/></svg></div>
<div class="slider-arrow outline" style="left:1116px;top:3410px"><svg width="14" height="14" viewBox="0 0 14 14"><path d="M5 2l5 5-5 5" fill="none" stroke="#3d8a88" stroke-width="2.4"/></svg></div>

<footer class="site-footer">
  <div class="footer-brand">
    <div class="brand-name">Dr. Jodel Brisk</div>
    <div class="brand-sub">Licensed Psychologist</div>
    <p>Lorem ipsum dolor sit amet, consectetur adipiscing elit, sed do eiusmod tempor incididunt ut labore et dolore magna aliqua. Quis ipsum nostrud exercitation ullamco.</p>
  </div>
  <div class="footer-col" style="left:446px">
    <h4>QUICK LINKS</h4>
    <ul><li>Home</li><li>About Us</li><li>Service</li><li>FAQs</li><li>Blog</li></ul>
  </div>
  <div class="footer-col" style="left:644px;width:240px">
    <h4>CONTACT US</h4>
    <div class="contact-item"><div class="contact-icon"><svg width="16" height="16" viewBox="0 0 16 16"><path d="M3 1h3l1 4-2 1c1 2 3 4 5 5l1-2 4 1v3c0 1-1 2-2 2C7 15 1 9 1 3c0-1 1-2 2-2z" fill="#fff"/></svg></div><div><b>PHONE NO:</b><span>(555) 014-2837</span></div></div>
    <div class="contact-item"><div class="contact-icon"><svg width="16" height="12" viewBox="0 0 16 12"><rect x="1" y="1" width="14" height="10" fill="none" stroke="#fff" stroke-width="1.6"/><path d="M1 1l7 6 7-6" fill="none" stroke="#fff" stroke-width="1.6"/></svg></div><div><b>EMAIL:</b><span>office@jodelbrisk.com</span></div></div>
    <div class="contact-item"><div class="contact-icon"><svg width="14" height="18" viewBox="0 0 14 18"><path d="M7 17S1 10 1 6.5a6 6 0 0 1 12 0C13 10 7 17 7 17z" fill="#fff"/><circle cx="7" cy="6.5" r="2.2" fill="#3d8a88"/></svg></div><div><b>LOCATION:</b><span>Lorem ipsum dolor sit amet, consetetur, USA</span></div></div>
  </div>
  <div class="footer-col" style="left:934px">
    <h4>FOLLOW US</h4>
    <div class="social"><i class="on"></i><i></i><i></i></div>
  </div>
</footer>
<div class="copyright">Copyright © 2025 Jodel Brisk Licensed Psychologist | All Rights Reserved</div>

</div>
</body>
</html>
```